Local Motorsports Photography Business Card Design

Looking for a Logo and Business Card design for my father who is a local photographer based in Perth operating under the business name "KLR Photography". Specializing in Motorsports (Torque Racers/Hyperwheels/Corvan Trial) and events photography.
Would like it to look professional, while still maintaining a local/personal feel. Color\Design of the Logo and Card are open to your own interpretation, but should limit the color scheme to around 2-3 colors.
Design should be a logo one side and contact details on the rear. The website currently is very simple and a generic template and should not be used as a basis for design.
Industry/Entity Type
Business
Contact Information for Business Card
Name: Malcolm Purdie
Website: www.klrphotography-example.com.au
Email: malcolm@klrphotography-example.com.au
Phone: 0471 629 385
Look and feel
Each slider illustrates characteristics of the customer's brand and the style your logo design should communicate.

```html
<!DOCTYPE html>
<html lang="en">
<head>
<meta charset="utf-8">
<title>KLR Photography – Business Card</title>
<link rel="stylesheet" href="https://fonts.googleapis.com/css2?family=Play:wght@400;700&display=swap">
<style>
  :root {
    --page-bg: #e9e9e9;
    --card-white: #ffffff;
    --blue-light: #7fcdf3;
    --blue-mid: #3fb0ea;
    --blue-deep: #1c97dc;
    --ink: #1e1e1e;
    --brand-blue: #2aa3e2;
    --on-blue: #ffffff;
  }
  * { box-sizing: border-box; margin: 0; padding: 0; }
  html, body {
    width: 1200px;
    height: 1085px;
    overflow: hidden;
    background: var(--page-bg);
    font-family: "Play", "Arial", sans-serif;
  }
  .card {
    position: absolute;
    left: 100px;
    top: 252px;
    width: 1000px;
    height: 580px;
    background: var(--card-white);
    overflow: hidden;
    box-shadow: 0 10px 30px rgba(0,0,0,0.18);
  }
  .card__wave {
    position: absolute;
    inset: 0;
    width: 1000px;
    height: 580px;
  }
  .contact {
    position: absolute;
    color: var(--on-blue);
    font-size: 21px;
    line-height: 1.35;
    letter-spacing: 0.5px;
    text-align: right;
    white-space: nowrap;
  }
  .contact--phone { right: 600px; top: 66px; }
  .contact--address { right: 530px; top: 142px; }
  .contact--web { right: 490px; top: 256px; }
  .contact-icon {
    position: absolute;
    width: 44px;
    height: 44px;
  }
  .contact-icon--phone { left: 418px; top: 71px; }
  .contact-icon--pin { left: 488px; top: 164px; }
  .contact-icon--globe { left: 528px; top: 262px; }
  .brand {
    position: absolute;
    left: 650px;
    top: 164px;
    display: flex;
    align-items: center;
    gap: 12px;
  }
  .brand__dot {
    width: 20px;
    height: 20px;
    border-radius: 50%;
    background: var(--brand-blue);
  }
  .brand__name {
    font-size: 34px;
    font-weight: 700;
    color: var(--brand-blue);
    white-space: nowrap;
  }
  .person {
    position: absolute;
    left: 682px;
    top: 270px;
    color: var(--ink);
    white-space: nowrap;
  }
  .person__name {
    font-size: 30px;
    letter-spacing: 2px;
    line-height: 1.1;
  }
  .person__role {
    font-size: 24px;
    line-height: 1.35;
  }
</style>
</head>
<body>
  <section class="card" aria-label="KLR Photography business card">
    <svg class="card__wave" viewBox="0 0 1000 580" aria-hidden="true">
      <defs>
        <radialGradient id="blueField" cx="0.3" cy="0.6" r="0.75">
          <stop offset="0" stop-color="#7fcdf3"/>
          <stop offset="0.55" stop-color="#3fb0ea"/>
          <stop offset="1" stop-color="#1c97dc"/>
        </radialGradient>
      </defs>
      <path fill="url(#blueField)"
        d="M0 0 H470 C505 25 470 60 500 100 C525 135 560 140 565 190 C570 235 560 250 590 285 C620 320 600 360 615 420 C628 470 620 530 640 580 H0 Z"/>
    </svg>

    <div class="contact contact--phone">0471 629 385<br>0471 629 385</div>
    <div class="contact contact--address">214,4th floor,<br>Kestrel Park Road<br>WA</div>
    <div class="contact contact--web">malcolm@klrphotography-example.com.au<br>www.klrphotography-example.com.au</div>

    <svg class="contact-icon contact-icon--phone" viewBox="0 0 44 44" aria-label="Phone">
      <circle cx="22" cy="22" r="19" fill="none" stroke="#ffffff" stroke-width="2.5"/>
      <path d="M15 13 l4 -1 l3 6 l-3 2 c1 3 3 5 6 6 l2 -3 l6 3 l-1 4 c-9 1 -18 -8 -17 -17z" fill="#ffffff"/>
    </svg>
    <svg class="contact-icon contact-icon--pin" viewBox="0 0 44 44" aria-label="Address">
      <circle cx="22" cy="22" r="19" fill="none" stroke="#ffffff" stroke-width="2.5"/>
      <path d="M22 32 C17 25 15 22 15 19 a7 7 0 0 1 14 0 c0 3 -2 6 -7 13z" fill="#ffffff"/>
      <circle cx="22" cy="19" r="2.6" fill="#3fb0ea"/>
    </svg>
    <svg class="contact-icon contact-icon--globe" viewBox="0 0 44 44" aria-label="Web">
      <circle cx="22" cy="22" r="19" fill="none" stroke="#ffffff" stroke-width="2.5"/>
      <g fill="none" stroke="#ffffff" stroke-width="1.8">
        <circle cx="22" cy="22" r="11"/>
        <ellipse cx="22" cy="22" rx="5" ry="11"/>
        <line x1="11" y1="22" x2="33" y2="22"/>
        <line x1="13" y1="16" x2="31" y2="16"/>
        <line x1="13" y1="28" x2="31" y2="28"/>
      </g>
    </svg>

    <div class="brand">
      <span class="brand__dot"></span>
      <span class="brand__name">KLR Photography</span>
    </div>

    <div class="person">
      <div class="person__name">MALCOLM PURDIE</div>
      <div class="person__role">Managing Director</div>
    </div>
  </section>
</body>
</html>
```